Brindmoor Gardening Fresh New Website

We are looking to create a simple fresh website for our landscaping business. The website should appeal to a 'high end' audience. We deal with a lot of Embassies and affluent clients who have extremely large gardens that are meticulously maintained. The site is about communicating our excellent landscaping and customer service skills and encouraging new clients to reach out and engage us to take care of their gardens.

The website is basically going to be our business card, it will have almost no functionality other than two 'contact us' forms, one for smaller clients and one for more detailed projects.

The website will not have a lot of written content and will have to show photos of beautifully landscaped gardens.

The main logo in black will influence the site, however, we are open to all suggestions.

We are expecting to have the following pages:
Home Page
Services
About Us
Contact Us
Showcase (photo gallery of our work)

We need someone who can code it to wordpress and be available for minor changes over a number of days. They will be simple tweaks.

```html
<!DOCTYPE html>
<html lang="en">
<head>
<meta charset="utf-8">
<title>Brindmoor Gardening</title>
<link rel="stylesheet" href="https://fonts.googleapis.com/css2?family=Lora:ital,wght@0,400;0,500;1,400&family=Lato:wght@400;700&display=swap">
<style>
:root{
  --green:#6aae3c;
  --green-dark:#4e8f26;
  --leaf-bg:#f3f9ea;
  --yellow:#f0bb00;
  --crimson:#ad0f3e;
  --ink:#2b2b2b;
  --dark:#2a2a2a;
  --footer:#262626;
  --muted:#8a8a8a;
  --line:#e3e3e3;
  --white:#fff;
}
*{box-sizing:border-box;margin:0;padding:0}
html,body{width:1200px;height:4201px;overflow:hidden}
body{position:relative;font-family:'Lato',sans-serif;color:var(--ink);background:var(--white);font-size:10px}
section,header,footer{position:absolute;left:0;width:1200px}
.abs{position:absolute}
.btn{position:absolute;display:flex;align-items:center;justify-content:center;font-size:7.5px;font-weight:700;letter-spacing:.4px;color:var(--white);text-transform:uppercase}
.btn.yellow{background:var(--yellow)}
.btn.green{background:var(--green)}
.photo{position:absolute}
.sec-title{position:absolute;font-family:'Lora',serif;font-size:20px;color:var(--ink)}
.sec-sub{position:absolute;font-size:9.5px;color:var(--muted)}
.center{left:0;width:1200px;text-align:center}

/* header */
.site-header{top:0;height:163px}
.grass-strip{position:absolute;top:0;left:0;width:1200px;height:33px;background:linear-gradient(180deg,#5ea22d,#86c24d)}
.brand{position:absolute;left:233px;top:48px;display:flex;align-items:center;gap:8px}
.brand-mark{width:14px;height:14px;border-radius:50%;background:var(--ink)}
.brand-name{font-family:'Lora',serif;font-size:13px;letter-spacing:3px;color:var(--ink);line-height:1.25;text-transform:uppercase}
.top-contact{position:absolute;top:62px;font-size:8px;color:#999;letter-spacing:.5px}
.top-contact b{display:block;font-weight:400;color:var(--yellow);font-size:9.5px;letter-spacing:0;margin-top:5px}
.top-contact svg{vertical-align:-2px;margin-right:4px}
.socials{position:absolute;top:62px;left:841px;display:flex;gap:7px}
.socials i{width:26px;height:26px;border:1px solid #555;border-radius:50%}
.main-nav{position:absolute;left:233px;top:121px;width:613px;height:42px;background:var(--leaf-bg);display:flex;align-items:center}
.main-nav span{position:absolute;font-size:10px;letter-spacing:.5px;color:var(--ink);text-transform:uppercase}
.main-nav span.active{color:var(--green)}
.quote-btn{left:846px;top:121px;width:119px;height:42px;font-size:8.5px}

/* hero */
.hero{top:163px;height:544px}
.hero-photo{left:0;top:0;width:1200px;height:544px;background:radial-gradient(ellipse at 55% 60%,#6f6d55 0%,#3e4a2c 35%,#22301a 70%,#1a2414 100%)}
.hero-kicker{position:absolute;left:233px;top:175px;font-family:'Lora',serif;font-style:italic;font-size:18px;color:var(--yellow)}
.hero-title{position:absolute;left:233px;top:210px;font-family:'Lora',serif;font-size:36px;line-height:48px;color:var(--white);letter-spacing:.5px;font-weight:400}
.hero .btn{top:321px;height:27px;font-size:7.5px}
.arrow{position:absolute;top:254px;width:36px;height:36px;border:1px solid rgba(255,255,255,.8);border-radius:50%;display:flex;align-items:center;justify-content:center}
.dots{position:absolute;top:505px;left:583px;display:flex;gap:6px}
.dots i{width:7px;height:7px;border-radius:50%;border:1px solid #ddd}
.dots i.on{border-color:var(--yellow)}

/* features */
.features{top:707px;height:467px}
.feature{position:absolute;top:93px;width:170px}
.feature .photo{position:static;width:170px;height:145px}
.feature h3{margin-top:25px;font-size:9px;font-weight:400;text-transform:uppercase;letter-spacing:.3px}
.feature p{margin-top:7px;font-size:9px;line-height:17px;color:var(--muted)}
.feature .btn{position:static;width:88px;height:27px;margin-top:17px}
.hours{position:absolute;left:796px;top:93px;width:169px;height:279px;border:1px solid var(--line);padding:24px 16px}
.hours h4{font-size:8.5px;font-weight:400;letter-spacing:.3px;text-transform:uppercase}
.hours p{margin-top:12px;font-size:8px;line-height:16px;color:var(--muted)}
.hours table{margin-top:12px;border-collapse:collapse;font-size:8px}
.hours td{height:24.5px;color:var(--muted)}
.hours td:first-child{color:var(--ink);width:52px}

/* about */
.about{top:1174px;height:374px;background:var(--leaf-bg)}
.about-photo{left:0;top:0;width:600px;height:374px;background:linear-gradient(160deg,#4f7a3a 0%,#3c6326 40%,#b48a5a 62%,#2f5520 100%)}
.about h2{position:absolute;left:644px;top:46px;font-family:'Lora',serif;font-size:20px;font-weight:400}
.about p{position:absolute;left:644px;width:400px;font-size:9.5px;line-height:17.5px;color:var(--muted)}
.stat{position:absolute;top:238px}
.stat strong{display:block;margin-top:8px;font-family:'Lora',serif;font-weight:400;font-size:19px}
.stat span{display:block;margin-top:2px;font-size:8.5px;letter-spacing:.4px;text-transform:uppercase}

/* services */
.services{top:1548px;height:493px}
.tab{position:absolute;left:235px;width:173px;height:36px;border:1px solid var(--line);display:flex;align-items:center;padding-left:22px;gap:12px;font-size:8px;text-transform:uppercase;letter-spacing:.3px}
.tab.on{color:var(--yellow)}
.svc-title{position:absolute;left:447px;top:176px;font-family:'Lora',serif;font-size:15px;font-weight:400}
.svc-text{position:absolute;left:447px;top:210px;width:330px;font-size:9.5px;line-height:17.5px;color:var(--muted)}
.svc-list{position:absolute;left:447px;top:276px;list-style:none;font-size:9px;color:var(--muted)}
.svc-list li{height:24px;display:flex;align-items:center;gap:12px}
.ivy{left:1030px;top:1548px;width:150px;height:620px;z-index:2;border-radius:60px;background:linear-gradient(180deg,rgba(106,174,60,.55),rgba(78,143,38,.35) 60%,rgba(90,140,50,0))}

/* gallery */
.gallery{top:2041px;height:543px;background:var(--dark)}
.gallery .sec-title,.gallery .sec-sub{color:var(--white)}
.grid{position:absolute;left:233px;top:179px;width:732px;display:grid;grid-template-columns:repeat(4,1fr);gap:2px}
.grid div{height:130px}

/* why */
.why{top:2584px;height:681px}
.reason{position:absolute;width:200px}
.reason h4{font-size:11px;font-weight:400;margin-top:12px}
.reason p{font-size:8.5px;line-height:18px;color:var(--muted);margin-top:8px}
.reason.right{text-align:right}
.why-photo{left:448px;top:234px;width:302px;height:310px;border:5px solid #c6c6c6;background:linear-gradient(170deg,#b9b48a 0%,#5f8c3a 35%,#3d6b22 70%,#8cae3b 100%)}

/* contact */
.contact{top:3265px;height:468px}
.quote-panel{position:absolute;left:0;top:0;width:730px;height:468px;background:var(--yellow)}
.touch-panel{position:absolute;left:730px;top:0;width:470px;height:468px;background:var(--green)}
.contact h2{position:absolute;top:98px;font-family:'Lora',serif;font-size:19px;font-weight:400;color:var(--white)}
.contact .lead{position:absolute;top:130px;font-size:9px;color:var(--white)}
.field{position:absolute;border-bottom:1px solid rgba(255,255,255,.8);font-size:7.5px;letter-spacing:.5px;color:var(--white);text-transform:uppercase;padding-bottom:7px}
.touch-item{position:absolute;left:33px;display:flex;gap:19px}
.touch-item .ring{width:40px;height:40px;border:1px solid var(--white);border-radius:50%;display:flex;align-items:center;justify-content:center;margin-top:38px}
.touch-item h5{font-family:'Lora',serif;font-size:12px;font-weight:400;color:var(--white)}
.touch-item p{margin-top:8px;font-size:9px;line-height:17px;color:var(--white)}

/* footer */
.site-footer{top:3733px;height:468px;background:var(--footer);color:var(--white)}
.alert-bar{position:absolute;left:231px;top:1px;width:732px;height:80px;background:var(--crimson)}
.alert{position:absolute;top:22px;display:flex;gap:17px}
.alert .ring{width:40px;height:40px;border:1px solid var(--white);border-radius:50%;display:flex;align-items:center;justify-content:center;margin-top:-4px}
.alert h5{font-family:'Lora',serif;font-size:12px;font-weight:400}
.alert p{font-size:8.5px;line-height:16px;margin-top:3px}
.foot-brand{position:absolute;left:233px;top:112px;display:flex;align-items:center;gap:8px}
.foot-brand .brand-mark{background:var(--white)}
.foot-brand .brand-name{color:var(--white)}
.foot-about{position:absolute;left:231px;top:195px;width:160px;font-size:9px;line-height:16.5px}
.foot-col h5{position:absolute;top:136px;font-family:'Lora',serif;font-size:12px;font-weight:400}
.foot-links{position:absolute;left:432px;top:169px;list-style:none;font-size:9px}
.foot-links li{height:21px}
.update{position:absolute;left:562px;display:flex;gap:15px}
.update .photo{position:static;width:51px;height:52px}
.update p{font-size:8.5px;line-height:15px;width:105px}
.update time{display:block;color:var(--yellow);font-size:7.5px;margin-top:2px}
.subscribe{position:absolute;left:784px;top:174px;width:178px;height:32px;background:#333;border:1px solid #3c3c3c;display:flex;align-items:center;justify-content:space-between;padding:0 14px;font-size:7.5px;color:#ccc}
.foot-socials{position:absolute;left:781px;top:277px;display:flex;gap:7px}
.foot-socials i{width:26px;height:26px;border:1px solid #666;border-radius:50%}
.foot-rule{position:absolute;left:231px;top:407px;width:734px;height:1px;background:#3a3a3a}
.copy{position:absolute;top:431px;left:0;width:1200px;text-align:center;font-size:7px;letter-spacing:.4px;color:#bbb;text-transform:uppercase}
</style>
</head>
<body>

<header class="site-header">
  <div class="grass-strip" role="img" aria-label="Strip of lawn grass along the top edge"></div>
  <div class="brand"><span class="brand-mark"></span><span class="brand-name">Brindmoor<br>Gardening</span></div>
  <div class="top-contact" style="left:557px">
    <svg width="10" height="8" viewBox="0 0 10 8"><rect x=".5" y=".5" width="9" height="7" fill="none" stroke="#999"/><path d="M.5 .5 5 4.5 9.5 .5" fill="none" stroke="#999"/></svg>EMAIL US
    <b>support@brindmoorgardening.com</b>
  </div>
  <div class="top-contact" style="left:722px">
    <svg width="9" height="9" viewBox="0 0 10 10"><path d="M2 1 4 3 3 4.5Q4.5 6.5 5.5 7L7 6 9 8 7.5 9.5Q3 9 .5 2.5Z" fill="none" stroke="#999"/></svg>CALL US
    <b>(+01) 123 456 7896</b>
  </div>
  <div class="socials"><i></i><i></i><i></i><i></i></div>
  <nav class="main-nav">
    <span class="active" style="left:25px">Home</span>
    <span style="left:91px">About Us</span>
    <span style="left:178px">Services</span>
    <span style="left:261px">Showcase</span>
    <span style="left:355px">Contact Us</span>
  </nav>
  <a class="btn yellow quote-btn">Get Free Quote</a>
</header>

<section class="hero">
  <div class="photo hero-photo" role="img" aria-label="Stone garden path winding through dense flowering plants"></div>
  <div class="arrow" style="left:60px"><svg width="8" height="10" viewBox="0 0 8 10"><path d="M6 1 2 5 6 9" fill="none" stroke="#fff" stroke-width="1.3"/></svg></div>
  <div class="arrow" style="left:1100px"><svg width="8" height="10" viewBox="0 0 8 10"><path d="M2 1 6 5 2 9" fill="none" stroke="#fff" stroke-width="1.3"/></svg></div>
  <p class="hero-kicker">Welcome to Brindmoor Gardening Services</p>
  <h1 class="hero-title">A BEAUTIFUL LAWN DOESN’T<br>HAPPEN BY ITSELF</h1>
  <a class="btn yellow" style="left:233px;width:109px">Purchase Now</a>
  <a class="btn green" style="left:349px;width:103px">Contact Now</a>
  <div class="dots"><i></i><i class="on"></i><i></i></div>
</section>

<section class="features">
  <article class="feature" style="left:233px">
    <div class="photo" role="img" aria-label="Green lawn mower cutting grass" style="background:linear-gradient(160deg,#2f4a22,#3f9a2a 55%,#7cc245)"></div>
    <h3>Lawn Maintenance</h3>
    <p>The tiny ship was tossed. If not for the courage of the fearless crew the Skiff would be lost.</p>
    <a class="btn yellow">Learn More</a>
  </article>
  <article class="feature" style="left:421px">
    <div class="photo" role="img" aria-label="Bed of pink and white flowers" style="background:linear-gradient(150deg,#3e6b2c,#6f9a4a 50%,#b88a98)"></div>
    <h3>Flower Scaping</h3>
    <p>The tiny ship was tossed. If not for the courage of the fearless crew the Skiff would be lost.</p>
    <a class="btn yellow">Learn More</a>
  </article>
  <article class="feature" style="left:608px">
    <div class="photo" role="img" aria-label="Curved brick walkway edged with stones and shrubs" style="background:linear-gradient(160deg,#5a8a3c,#8f6a52 50%,#6c9a4a)"></div>
    <h3>Natural Stone Walks</h3>
    <p>The tiny ship was tossed. If not for the courage of the fearless crew the Skiff would be lost.</p>
    <a class="btn yellow">Learn More</a>
  </article>
  <aside class="hours">
    <h4>Working Hours</h4>
    <p>Here he comes Here is comes<br>Swift Rider he's a demon</p>
    <table>
      <tr><td>Monday</td><td>8:00am - 7:00pm</td></tr>
      <tr><td>Tuesday</td><td>8:00am - 7:00pm</td></tr>
      <tr><td>Wednesday</td><td>8:00am - 7:00pm</td></tr>
      <tr><td>Thurday</td><td>8:00am - 7:00pm</td></tr>
      <tr><td>Friday</td><td>8:00am - 7:00pm</td></tr>
      <tr><td>Saturday</td><td>8:00am - 4:00pm</td></tr>
      <tr><td>Sunday</td><td>Closed</td></tr>
    </table>
  </aside>
</section>

<section class="about">
  <div class="photo about-photo" role="img" aria-label="Greenhouse garden with a sandy path and wooden bench"></div>
  <h2>About Us</h2>
  <p style="top:86px">Lorem Ipsum is simply dummy text of the printing and typesetting industry. Lorem Ipsum has been the industry's standard dummy text ever since the 1500s</p>
  <p style="top:133px">Lorem Ipsum is simply dummy text of the printing and typesetting industry. Lorem Ipsum has been the industry's standard dummy text ever since the 1500s Lorem Ipsum is simply dummy text of the printing and typesetting industry. Lorem Ipsum has</p>
  <div class="stat" style="left:644px">
    <svg width="24" height="24" viewBox="0 0 24 24" fill="none" stroke="#f0bb00" stroke-width="1.4"><path d="M12 22V8M12 12 7 7M12 15 17 10M12 18 7 14M12 9 16 4"/></svg>
    <strong>999</strong><span>Happy Clients</span>
  </div>
  <div class="stat" style="left:782px">
    <svg width="24" height="24" viewBox="0 0 24 24" fill="none" stroke="#f0bb00" stroke-width="1.4"><path d="M3 21 14 10M14 10l4-6 3 3-6 4z"/><circle cx="6" cy="18" r="2"/></svg>
    <strong>1,589</strong><span>Completed Works</span>
  </div>
  <div class="stat" style="left:947px">
    <svg width="24" height="24" viewBox="0 0 24 24" fill="none" stroke="#f0bb00" stroke-width="1.4"><path d="M12 20V10M12 12c-5 0-7-3-7-7 4 0 7 2 7 7zM12 12c4 0 7-2 7-6-4 0-7 2-7 6zM4 20h16"/></svg>
    <strong>215</strong><span>Awards &amp; Honors</span>
  </div>
</section>

<section class="services">
  <h2 class="sec-title" style="left:233px;top:95px;font-weight:400">Our Services</h2>
  <p class="sec-sub" style="left:233px;top:127px">very best to make the others comfortable in their tropic</p>
  <div class="tab" style="top:181px"><svg width="16" height="14" viewBox="0 0 16 14" fill="none" stroke="#6aae3c"><circle cx="4" cy="10" r="3"/><path d="M7 8 13 2M11 2h3v3"/></svg>Lawn Renovation</div>
  <div class="tab on" style="top:225px"><svg width="16" height="14" viewBox="0 0 16 14" fill="none" stroke="#6aae3c"><path d="M2 3v10M6 3v10M10 3v10M14 3v10M1 6h14M1 10h14"/></svg>Lawn Moving</div>
  <div class="tab" style="top:269px"><svg width="16" height="14" viewBox="0 0 16 14" fill="none" stroke="#6aae3c"><path d="M2 10h8l4-5M4 10V7h5v3"/><circle cx="14" cy="3" r="1"/></svg>Watering Garden</div>
  <div class="tab" style="top:313px"><svg width="16" height="14" viewBox="0 0 16 14" fill="none" stroke="#6aae3c"><circle cx="6" cy="6" r="4"/><path d="M6 10v3M10 8l4 4"/></svg>Garden Care</div>
  <div class="tab" style="top:357px"><svg width="16" height="14" viewBox="0 0 16 14" fill="none" stroke="#6aae3c"><path d="M3 12 12 3M6 3l6 6M3 6l5 5"/></svg>Tree Trimming</div>
  <h3 class="svc-title">Lawn Moving</h3>
  <p class="svc-text">Flying away on a wing and a prayer. Who could it be. Believe it or not its just me! Space. The final frontier. These are the voyages of the Starship Meridian. Believe it or not I'm walking on air.</p>
  <ul class="svc-list">
    <li><svg width="16" height="10" viewBox="0 0 16 10" fill="none" stroke="#6aae3c"><path d="M1 5q7-7 14 0q-7 7-14 0z"/><circle cx="8" cy="5" r="1.5"/></svg>Our experts will take care of your lawn</li>
    <li><svg width="16" height="10" viewBox="0 0 16 10" fill="none" stroke="#6aae3c"><path d="M1 5q7-7 14 0q-7 7-14 0z"/><circle cx="8" cy="5" r="1.5"/></svg>We use latest technology to move your lawn</li>
    <li><svg width="16" height="10" viewBox="0 0 16 10" fill="none" stroke="#6aae3c"><path d="M1 5q7-7 14 0q-7 7-14 0z"/><circle cx="8" cy="5" r="1.5"/></svg>After moving lawn our team will maintain your lawn</li>
  </ul>
  <a class="btn yellow" style="left:447px;top:361px;width:88px;height:27px">Learn More</a>
</section>

<div class="abs ivy" role="img" aria-label="Hanging ivy vine decoration"></div>

<section class="gallery">
  <h2 class="sec-title center" style="top:94px;font-weight:400">Our Project Gallery</h2>
  <p class="sec-sub center" style="top:125px;color:#fff">They really scream haunted household</p>
  <div class="grid">
    <div role="img" aria-label="Watering a flowering shrub" style="background:linear-gradient(160deg,#1f4a5a,#6a8a6a 60%,#c9c4a8)"></div>
    <div role="img" aria-label="Greenhouse full of climbing plants" style="background:linear-gradient(160deg,#dfe8d8,#5a8a3a 60%,#2f5a20)"></div>
    <div role="img" aria-label="Tropical garden with palms and path" style="background:linear-gradient(160deg,#3a5a2a,#7a9a3a 55%,#c8a040)"></div>
    <div role="img" aria-label="Garden walkway beside a building" style="background:linear-gradient(160deg,#8aa8c0,#6a9a4a 55%,#b06a5a)"></div>
    <div role="img" aria-label="Rows of potted plants in a greenhouse" style="background:linear-gradient(160deg,#4a4a3a,#9aa07a 50%,#b05a50)"></div>
    <div role="img" aria-label="Potted plants inside a glasshouse" style="background:linear-gradient(160deg,#6a7a5a,#3f6a2f 55%,#9a6a4a)"></div>
    <div role="img" aria-label="Gardener tending plants in a greenhouse" style="background:linear-gradient(160deg,#c8d0c0,#4a7a3a 55%,#2a4a20)"></div>
    <div role="img" aria-label="Hillside garden path with mountain view" style="background:linear-gradient(180deg,#9ab0c8,#4a7a3a 45%,#2f5a22)"></div>
  </div>
</section>

<section class="why">
  <h2 class="sec-title center" style="top:92px;font-weight:400">Why Choose US</h2>
  <p class="sec-sub center" style="top:125px">very best makeot comfortable</p>

  <div class="reason" style="left:233px;top:222px">
    <svg width="30" height="28" viewBox="0 0 30 28" fill="none" stroke="#6aae3c" stroke-width="1.4"><path d="M4 24h22M15 24V13M15 15c-7 0-10-4-10-10 6 0 10 3 10 10zM15 13c5 0 9-3 9-9-5 0-9 3-9 9z"/></svg>
    <h4>Over 20 Years Experience</h4><p>The mate was a mighty sailin' man skipper<br>to sure five passengers</p>
  </div>
  <div class="reason" style="left:233px;top:354px">
    <svg width="30" height="28" viewBox="0 0 30 28" fill="none" stroke="#6aae3c" stroke-width="1.4"><path d="M4 26V6l2-3 2 3v20M12 26V6l2-3 2 3v20M20 26V6l2-3 2 3v20M2 11h26M2 20h26"/></svg>
    <h4>Licensed &amp; Insured</h4><p>The mate was a mighty sailin' man skipper<br>to sure five passengers</p>
  </div>
  <div class="reason" style="left:233px;top:478px">
    <svg width="34" height="28" viewBox="0 0 34 28" fill="none" stroke="#6aae3c" stroke-width="1.4"><path d="M3 3l8 12h16v5H9M11 15l-2-5"/><circle cx="11" cy="22" r="3"/><circle cx="26" cy="22" r="3"/></svg>
    <h4>Excellent Services</h4><p>The mate was a mighty sailin' man skipper<br>to sure five passengers</p>
  </div>

  <div class="reason right" style="left:765px;top:222px">
    <svg width="30" height="28" viewBox="0 0 30 28" fill="none" stroke="#6aae3c" stroke-width="1.4"><path d="M4 4l14 14M10 4l8 8M18 18l6 6M24 18l-6 6"/></svg>
    <h4>Expert Operators</h4><p>The mate was a mighty sailin' man skipper<br>to sure five passengers</p>
  </div>
  <div class="reason right" style="left:765px;top:354px">
    <svg width="30" height="28" viewBox="0 0 30 28" fill="none" stroke="#6aae3c" stroke-width="1.4"><circle cx="14" cy="11" r="8"/><path d="M14 19v7M10 26h8M10 12c2 2 6 2 8-2"/></svg>
    <h4>100+ Happy Customers</h4><p>The mate was a mighty sailin' man skipper<br>to sure five passengers</p>
  </div>
  <div class="reason right" style="left:765px;top:478px">
    <svg width="36" height="28" viewBox="0 0 36 28" fill="none" stroke="#6aae3c" stroke-width="1.4"><path d="M2 8h22l-4 10H8zM24 8l4-4h6"/><circle cx="10" cy="23" r="3"/></svg>
    <h4>Quality &amp; Reliability</h4><p>The mate was a mighty sailin' man skipper<br>to sure five passengers</p>
  </div>

  <div class="photo why-photo" role="img" aria-label="Gardener in a cap trimming a rounded hedge"></div>
</section>

<section class="contact">
  <div class="quote-panel">
    <h2 style="left:233px">Get a Quick Quote</h2>
    <p class="lead" style="left:233px">very best to make the others comfortable in their tropic</p>
    <div class="field" style="left:233px;top:168px;width:148px">Your Name</div>
    <div class="field" style="left:399px;top:168px;width:148px">Your Email</div>
    <div class="field" style="left:233px;top:206px;width:148px">Phone</div>
    <div class="field" style="left:399px;top:206px;width:148px;display:flex;justify-content:space-between">Lawn Moving<svg width="8" height="6" viewBox="0 0 8 6"><path d="M1 1l3 3 3-3" fill="none" stroke="#fff"/></svg></div>
    <div class="field" style="left:233px;top:244px;width:314px;height:78px">Message</div>
    <a class="btn green" style="left:233px;top:349px;width:96px;height:27px">Get a Quote</a>
  </div>
  <div class="touch-panel">
    <h2 style="left:31px">Get In Touch With Us</h2>
    <p class="lead" style="left:31px">very best to make the others comfortable in their tropic</p>
    <div class="touch-item" style="top:169px">
      <div class="ring"><svg width="14" height="16" viewBox="0 0 14 16" fill="none" stroke="#fff"><path d="M7 15s5-5 5-9A5 5 0 0 0 2 6c0 4 5 9 5 9z"/><circle cx="7" cy="6" r="2"/></svg></div>
      <div><h5>Address</h5><p>Lorem Ipsum is simply dummy<br>text of the printing and typeset-</p></div>
    </div>
    <div class="touch-item" style="top:251px">
      <div class="ring"><svg width="14" height="14" viewBox="0 0 10 10" fill="none" stroke="#fff"><path d="M2 1 4 3 3 4.5Q4.5 6.5 5.5 7L7 6 9 8 7.5 9.5Q3 9 .5 2.5Z"/></svg></div>
      <div><h5>Call Us</h5><p>+(01) 123 456 7896 &nbsp; (or)<br>+(01) 123 456 7899</p></div>
    </div>
    <div class="touch-item" style="top:333px">
      <div class="ring"><svg width="16" height="12" viewBox="0 0 16 12" fill="none" stroke="#fff"><rect x=".5" y=".5" width="15" height="11"/><path d="M.5 .5 8 7l7.5-6.5"/></svg></div>
      <div><h5>Mail Us</h5><p>info@brindmoorgardening.com<br>help@brindmoorgardening.com</p></div>
    </div>
  </div>
</section>

<footer class="site-footer">
  <div class="alert-bar">
    <div class="alert" style="left:19px">
      <div class="ring"><svg width="14" height="16" viewBox="0 0 14 16" fill="none" stroke="#fff"><path d="M7 15s5-5 5-9A5 5 0 0 0 2 6c0 4 5 9 5 9z"/><circle cx="7" cy="6" r="2"/></svg></div>
      <div><h5>Contact Us</h5><p>Lorem Ipsum is simply dummy<br>text of the printing and typeset-</p></div>
    </div>
    <div class="alert" style="left:263px">
      <div class="ring"><svg width="14" height="14" viewBox="0 0 10 10" fill="none" stroke="#fff"><path d="M2 1 4 3 3 4.5Q4.5 6.5 5.5 7L7 6 9 8 7.5 9.5Q3 9 .5 2.5Z"/></svg></div>
      <div><h5>Any Emergency</h5><p>+(01) 123 456 7896 &nbsp;(or)<br>+(01) 123 456 7896</p></div>
    </div>
    <div class="alert" style="left:509px">
      <div class="ring"><svg width="16" height="12" viewBox="0 0 16 12" fill="none" stroke="#fff"><rect x=".5" y=".5" width="15" height="11"/><path d="M.5 .5 8 7l7.5-6.5"/></svg></div>
      <div><h5>Get a Quick Quote</h5><p>info@brindmoorgardening (or)<br>support@brindmoorgardening</p></div>
    </div>
  </div>

  <div class="foot-brand"><span class="brand-mark"></span><span class="brand-name">Brindmoor<br>Gardening</span></div>
  <p class="foot-about">Lorem Ipsum is simply dummy text of the printing and typesetting industry. Lorem Ipsum has been the industry's standard dummy text ever since the 1500</p>

  <div class="foot-col"><h5 style="left:432px">Quick Links</h5></div>
  <ul class="foot-links"><li>About Us</li><li>Services</li><li>showcase</li><li>Contact Us</li></ul>

  <div class="foot-col"><h5 style="left:561px">Latest Updates</h5></div>
  <div class="update" style="top:173px">
    <div class="photo" role="img" aria-label="Garden shears among flowers" style="background:linear-gradient(150deg,#8a6a4a,#b04a3a 60%,#5a7a3a)"></div>
    <p>Movin' on up to the east finally got a piece<time>Feb 25, 2024</time></p>
  </div>
  <div class="update" style="top:241px">
    <div class="photo" role="img" aria-label="Hands planting a seedling" style="background:linear-gradient(150deg,#5a7aa0,#8a7a5a 60%,#4a6a3a)"></div>
    <p>Started from this tropi caboard this tiny ship<time>Feb 21, 2024</time></p>
  </div>
  <div class="update" style="top:309px">
    <div class="photo" role="img" aria-label="Watering can on soil" style="background:linear-gradient(150deg,#a08a6a,#6a5a4a 60%,#c0a080)"></div>
    <p>Gee our old roadster ran great: were the days<time>March 15, 2024</time></p>
  </div>

  <div class="foot-col"><h5 style="left:781px">Subscribe</h5></div>
  <div class="subscribe">Email Address<svg width="10" height="10" viewBox="0 0 10 10"><path d="M1 5 9 1 6 9 5 5z" fill="#6aae3c"/></svg></div>
  <div class="foot-col"><h5 style="left:781px;top:247px">Connect With Us</h5></div>
  <div class="foot-socials"><i></i><i></i><i></i><i></i></div>

  <div class="foot-rule"></div>
  <p class="copy">© 2024 Brindmoor Gardening All Rights Reserved</p>
</footer>

</body>
</html>
```